Etiketten-Design für Qualitäts- und Prädikatswein
Zielgruppe
Qualitäts- und Prädikatsweine
Aufgabenstellung
Das Etikett muss auf der Weinflasche zweigeteilt sein.
Etikett vorne: Höhe 14,5 cm x Breite 6 cm:
Auf der Vorderseite sollen folgende Daten mit enthalten sein (Reihenfolge ist frei wählbar):
- Unser Logo (Datei: Logo)
- Name des Weins z.B. Velora
- Kategorie z.B. Beerenauslese
- Geschmackskategorie z.B. süß
- Jahrgang z.B. 2023
- Austria
Rückenetikett (Beispiel: Datei Rückenetikett): Höhe 11 cm x Breite 6 cm
Auf der Rückseite müssen folgende Daten vorhanden sein (Reihenfolge ist frei wählbar):
- Logo ganz oben
- Verkehrsbezeichnungen (Schriftgröße mind. 1,2 mm): Prädikatswein LN 4827163
- Herkunft (Schriftgröße mind. 1,2 mm): Wein aus Österreich Burgenland
- Nennvolumen (Schriftgröße mind. 6 mm): e 0,5 L
- Alkoholgehalt (Schriftgröße mind. 1,2 mm): Alc. 8,5 % Vol.
- Restzuckergehalt (Schriftgröße mind. 1,2 mm): süß
- Zutaten (Schriftgröße mind. 1,2 mm): Zutaten und ein QR-Code
- Platz für ein Zertifizierungslogo
- Allergenkennzeichnung (Schriftgröße mind. und max. 1,2 mm): Enthält Sulfite
- Abfüller (Schriftgröße mind. 1,2 mm):
Vertrieb:
Kalmor Nerisa GmbH
A-4638 Gols
www.kalmor-nerisa.com
Abfüller 5361842 A-4638 <---- (Schriftgröße mind. und max. 1,2 mm)
Kalmor Solenn ArtikelNr.: 3815/46
Da wir vor allem Prädikatsweine mit höchster Qualität herstellen, soll das Etikett dies auch wiederspiegeln. Den Hintergrund stellen wir uns schwarz vor. Der Hintergrund darf auch gerne eine grafische Musterrung beinhalten.
Alle Angaben müssen sich in den Dateien bearbeitbar sein, da sich diese Daten zum teil noch ändern werden. Die Dateien müssen wir Druckereien geeignet sein.
Update: Das Flaschenmaß ist Höhe 30 cm, Durchmesser unten 6 cm. Es handelt sich also um eine schlanke Flasche. Siehe Datei: Flasche

```html
<!DOCTYPE html>
<html lang="de">
<head>
<meta charset="utf-8">
<title>Velora – Beerenauslese Etikett</title>
<link rel="stylesheet" href="https://fonts.googleapis.com/css2?family=Bodoni+Moda:wght@400&family=Cinzel:wght@400&family=Lato:wght@300;400&family=Playfair+Display:ital@1&display=swap">
<style>
  :root {
    --page: #ffffff;
    --label-deep: #121212;
    --label-mid: #3c3c3c;
    --label-sheen: #6a6a6a;
    --ink-light: #f2f2f2;
    --ink-soft: #d8d8d8;
    --rule: #9a9a9a;
    --vintage-red: #b0141f;
    --muted: #8a8a8a;
    --gold-1: #8a6d12;
    --gold-2: #d9b43a;
    --leaf-1: rgba(120,120,120,0.45);
    --leaf-2: rgba(40,40,40,0);
  }
  * { box-sizing: border-box; }
  html, body {
    margin: 0;
    width: 1040px;
    height: 1200px;
    overflow: hidden;
    background: var(--page);
  }
  .canvas {
    position: relative;
    width: 1040px;
    height: 1200px;
  }
  .front-label {
    position: absolute;
    left: 298px;
    top: 59px;
    width: 444px;
    height: 1082px;
  }
  .label-shape {
    position: absolute;
    inset: 0;
    width: 444px;
    height: 1082px;
  }
  .grape-emblem {
    position: absolute;
    left: 176px;
    top: 14px;
    width: 92px;
    height: 88px;
    clip-path: polygon(0 0, 100% 0, 50% 100%);
    background: linear-gradient(180deg, var(--gold-2), var(--gold-1));
  }
  .brand-mark {
    position: absolute;
    left: 202px;
    top: 205px;
    width: 40px;
    height: 40px;
    border-radius: 50%;
    border: 1.5px solid var(--ink-soft);
  }
  .brand-name {
    position: absolute;
    left: 0;
    width: 100%;
    top: 258px;
    margin: 0;
    text-align: center;
    font-family: "Cinzel", serif;
    font-size: 26px;
    color: var(--ink-light);
    letter-spacing: 0.5px;
  }
  .rule {
    position: absolute;
    left: 33px;
    width: 378px;
    height: 1px;
    background: var(--rule);
  }
  .rule-top { top: 405px; }
  .rule-bottom { top: 494px; }
  .wine-name {
    position: absolute;
    left: 0;
    width: 100%;
    top: 410px;
    margin: 0;
    text-align: center;
    font-family: "Bodoni Moda", serif;
    font-weight: 400;
    font-size: 66px;
    line-height: 80px;
    color: var(--ink-light);
    letter-spacing: 2px;
  }
  .category {
    position: absolute;
    left: 0;
    width: 100%;
    top: 526px;
    margin: 0;
    text-align: center;
    font-family: "Lato", sans-serif;
    font-weight: 400;
    font-size: 20px;
    letter-spacing: 3px;
    color: var(--ink-soft);
  }
  .vine-leaves {
    position: absolute;
    left: 222px;
    top: 546px;
    width: 222px;
    height: 425px;
    background: radial-gradient(ellipse at 55% 45%, var(--leaf-1), var(--leaf-2) 72%);
  }
  .vintage {
    position: absolute;
    left: 114px;
    width: 160px;
    top: 626px;
    margin: 0;
    text-align: center;
    font-family: "Playfair Display", serif;
    font-style: italic;
    font-size: 26px;
    letter-spacing: 6px;
    color: var(--vintage-red);
  }
  .taste {
    position: absolute;
    left: 114px;
    width: 160px;
    top: 676px;
    margin: 0;
    text-align: center;
    font-family: "Lato", sans-serif;
    font-size: 15px;
    letter-spacing: 4px;
    color: var(--vintage-red);
  }
  .vine-tree {
    position: absolute;
    left: 139px;
    top: 829px;
    width: 139px;
    height: 92px;
    border-radius: 50% 50% 8px 8px;
    background: radial-gradient(ellipse at 50% 40%, rgba(200,200,200,0.55), rgba(120,120,120,0) 70%);
  }
  .origin {
    position: absolute;
    left: 114px;
    width: 190px;
    top: 934px;
    margin: 0;
    text-align: center;
    font-family: "Lato", sans-serif;
    font-weight: 300;
    font-size: 15px;
    letter-spacing: 9px;
    color: var(--muted);
  }
</style>
</head>
<body>
<main class="canvas">
  <section class="front-label" aria-label="Vorderetikett Velora Beerenauslese">
    <svg class="label-shape" viewBox="0 0 240 585" preserveAspectRatio="none" aria-hidden="true">
      <defs>
        <linearGradient id="labelSheen" x1="0" y1="0" x2="1" y2="0">
          <stop offset="0" stop-color="#1a1a1a"/>
          <stop offset="0.12" stop-color="#4a4a4a"/>
          <stop offset="0.22" stop-color="#6a6a6a"/>
          <stop offset="0.34" stop-color="#2a2a2a"/>
          <stop offset="0.55" stop-color="#141414"/>
          <stop offset="0.75" stop-color="#3a3a3a"/>
          <stop offset="0.9" stop-color="#222222"/>
          <stop offset="1" stop-color="#101010"/>
        </linearGradient>
        <linearGradient id="tabSheen" x1="0" y1="0" x2="1" y2="0">
          <stop offset="0" stop-color="#1c1c1c"/>
          <stop offset="0.5" stop-color="#4a4a4a"/>
          <stop offset="1" stop-color="#1c1c1c"/>
        </linearGradient>
      </defs>
      <path class="label-body" fill="url(#labelSheen)"
        d="M6 47 H58 L120 106 L182 47 H234 Q240 47 240 53 V540 Q240 546 234 548 L120 584 L6 548 Q0 546 0 540 V53 Q0 47 6 47 Z"/>
      <path class="label-tab" fill="url(#tabSheen)"
        d="M74 0 H166 Q174 0 170 7 L124 76 Q120 81 116 76 L70 7 Q66 0 74 0 Z"/>
    </svg>

    <div class="grape-emblem" role="img" aria-label="Goldene Weintrauben-Grafik"></div>

    <div class="brand-mark" aria-hidden="true"></div>
    <p class="brand-name">Kalmor Solenn</p>

    <div class="rule rule-top"></div>
    <h1 class="wine-name">VELORA</h1>
    <div class="rule rule-bottom"></div>

    <p class="category">BEERENAUSLESE</p>

    <div class="vine-leaves" role="img" aria-label="Weinblätter und Traube als dezente graue Illustration"></div>

    <p class="vintage">2·0·2·3</p>
    <p class="taste">süß</p>

    <div class="vine-tree" role="img" aria-label="Gezeichneter Rebstock"></div>

    <p class="origin">AUSTRIA</p>
  </section>
</main>
</body>
</html>
```